Blue Ladle Handcrafted Tomato Ketchup packaging design modern

From the best ingredients there is the best ketchup Blue Handcrafted ketchup are specially formulated for fine dining and drinks, bringing out all the flavors. As the Blue Ladle handcrafted ketchup is otherwise fabulous: Made with wholesome, fully ripe fruits Nothing with half things! All Blue Ladle handcrafted ketchups are pure nature, without any artificial diluents or concentrates. Where tomato is on it, that's all there is to it - guaranteed! the design should be professional and noble despite being trendy. A watcher wants to sell the ketchup as merchandising from our restaurant. but as a single brand positioning. The ketchup is vegan. Dimensions: 6.8 cm Height: 7.8 cm Circumference: 21.6 cm The text down (Text 1-4). The lid of the text the glass packaging is black! Thanks for your efforts. I look forward to your designs.

Target Market(s)

foodies

Font styles to use
Serif
Sans Serif

Colors

Designer to choose colors to be used in the design.

Requirements
Must have
• Title: (Handcrafted Tomato Ketchup) Text One: (Store chilled after opening and consume quickly, pasteurized.) Text Two: (Handcrafted in Switzerland by Brennwald Kulinarik GmbH, Chur www.blueladle-sample.ch) Text Tree: (Tomatoes, White Wine Vinegar, Aceto Balsamico, Brown Cane Sugar, Corn Starch, Spices, Salt) Text For: (200 grams) or (200g) The Logo of Blue Ladle with the Pasta and Wine have to because of the gesety.
Nice to have
• small vegan icon (maybe)
Should not have
• text of the logo (pasta & wine)

```html
<!DOCTYPE html>
<html lang="de">
<head>
<meta charset="utf-8">
<title>Blue Ladle – Handcrafted Tomato Ketchup Label</title>
<link rel="stylesheet" href="https://fonts.googleapis.com/css2?family=Special+Elite&family=Courier+Prime&family=Josefin+Sans:wght@400&display=swap">
<style>
  :root {
    --canvas-bg: #efefec;
    --label-bg: #ffffff;
    --ink: #2b2b2b;
    --ink-soft: #555555;
    --accent: #c8435d;
    --rule: #3a3a3a;
  }
  * { box-sizing: border-box; margin: 0; padding: 0; }
  html, body { width: 1200px; height: 867px; overflow: hidden; background: var(--canvas-bg); }
  .canvas {
    position: relative; width: 1200px; height: 867px;
    display: flex; align-items: center; justify-content: center; gap: 60px;
  }
  .label {
    position: relative; width: 460px; height: 270px;
    background: var(--label-bg); color: var(--ink);
    box-shadow: 0 1px 3px rgba(0,0,0,.08);
  }

  /* Front label */
  .brand-row {
    position: absolute; top: 36px; left: 0; right: 0;
    display: flex; align-items: center; gap: 12px;
  }
  .brand-row .rule { flex: 1; height: 1.5px; background: var(--rule); position: relative; }
  .brand-row .rule--left::before,
  .brand-row .rule--right::after {
    content: ""; position: absolute; top: 0; width: 1.5px; height: 7px; background: var(--rule);
  }
  .brand-row .rule--left::before { left: 22px; }
  .brand-row .rule--right::after { right: 22px; }
  .brand-name {
    font-family: "Josefin Sans", sans-serif; font-size: 22px;
    letter-spacing: 3px; text-transform: uppercase; line-height: 1; padding-top: 4px;
  }
  .product-title {
    position: absolute; top: 82px; left: 0; right: 0; text-align: center;
    font-family: "Special Elite", monospace; font-size: 66px; letter-spacing: 6px; line-height: 1;
  }
  .title-rule {
    position: absolute; top: 190px; left: 50%; width: 200px; margin-left: -100px;
    height: 1.5px; background: var(--rule);
  }
  .product-sub {
    position: absolute; top: 218px; left: 0; right: 0; text-align: center;
    font-family: "Courier Prime", monospace; font-size: 19px; letter-spacing: .5px;
  }

  /* Back label */
  .info {
    position: absolute; top: 30px; left: 0; width: 350px;
    font-family: "Courier Prime", monospace; font-size: 14.5px; line-height: 1.25;
  }
  .info-block { padding: 8px 14px 8px 8px; border-bottom: 1.5px solid var(--rule); }
  .info-block:last-child { border-bottom: none; }
  .info-block--ingredients { color: var(--accent); }
  .divider {
    position: absolute; top: 30px; bottom: 30px; left: 350px; width: 1.5px; background: var(--rule);
  }
  .badges {
    position: absolute; top: 34px; left: 352px; right: 0;
    display: flex; flex-direction: column; align-items: center; gap: 10px;
  }
  .net-weight {
    position: absolute; bottom: 40px; right: 12px;
    font-family: "Courier Prime", monospace; font-size: 17px; color: var(--accent);
  }
</style>
</head>
<body>
<main class="canvas">

  <section class="label label--front" aria-label="Vorderseite Etikett">
    <div class="brand-row">
      <span class="rule rule--left"></span>
      <span class="brand-name">Blue Ladle</span>
      <span class="rule rule--right"></span>
    </div>
    <h1 class="product-title">Titel</h1>
    <div class="title-rule"></div>
    <p class="product-sub">[Handcrafted Tomato Ketchup]</p>
  </section>

  <section class="label label--back" aria-label="Rückseite Etikett">
    <div class="info">
      <p class="info-block">Nach dem Öffnen gekühlt aufbewahren und rasch konsumieren</p>
      <p class="info-block">Handcrafted in Switzerland by Brennwald Kulinarik GmbH, Chur</p>
      <p class="info-block">www.blueladle-sample.ch</p>
      <p class="info-block info-block--ingredients">Tomaten, Weissweinessig, Aceto Balsamico, brauner Rohrzucker, Maisstärke, Gewürze, Salz</p>
    </div>
    <div class="divider"></div>
    <div class="badges">
      <svg class="badge badge--vegan" width="52" height="52" viewBox="0 0 52 52" role="img" aria-label="Vegan-Zertifikat">
        <circle cx="26" cy="26" r="23" fill="none" stroke="var(--ink-soft)" stroke-width="2"/>
      </svg>
      <svg class="badge badge--organic" width="60" height="60" viewBox="0 0 60 60" role="img" aria-label="Bio-Zertifikat">
        <circle cx="30" cy="30" r="27" fill="none" stroke="var(--ink-soft)" stroke-width="1.5"/>
        <circle cx="30" cy="30" r="17" fill="none" stroke="var(--ink-soft)" stroke-width="1.5"/>
      </svg>
    </div>
    <p class="net-weight">200 Gramm</p>
  </section>

</main>
</body>
</html>
```